Design a PRODUCT TAG for backpackers and travellers equipment/accessories company

We need a Tag Design for our products. We are a new company based in the UK called 'RoamNest'. We produce travel equipment and accessories for backpackers. Our customers are young (18-30) individuals usually GAP year makers or young professionals who enjoy travelling, adventures and exploring the world. The Tag must state our name RoamNest (at the front) and Logo(at the front) and website address www.roamnest-example.uk (on the back) and communicate our company's aim of making backpackers trip hassle free where full attention is concentrated on adventure and fun.

Target Market(s)

Young individual passionate about travelling. 18-30 age. UNI students, gap year makers or young professionals

Industry/Entity Type

Travel Industry

Colors
3276b5
33a6d7
33b8a4
abd036
fbee3d
fece3e
f68d4d
0592cd
85cae6

Requirements
Must have
• The logo and on the front
• The web address at the back
• Half of the back should be black in order to fit the product label
Nice to have
• Would be nice for the design to look like something related to travel, so for example like a plain ticket, or passport, or anything else that can be related to holiday making and travelling.

```html
<!DOCTYPE html>
<html lang="en">
<head>
<meta charset="utf-8">
<title>RoamNest Product Tag</title>
<link rel="stylesheet" href="https://fonts.googleapis.com/css2?family=PT+Sans:wght@400;700&family=PT+Sans+Narrow:wght@400;700&display=swap">
<style>
  :root {
    --page-bg: #e9e6e2;
    --sky-top: #b98634;
    --sky-mid: #d9792a;
    --sky-glow: #e0561c;
    --ground: #2e1d15;
    --ground-deep: #1c120e;
    --band-orange: rgba(224, 78, 22, 0.85);
    --band-dark: rgba(36, 20, 14, 0.82);
    --rule-white: #fbf8f3;
    --ink-dark: #231a16;
    --ghost: rgba(70, 45, 25, 0.2);
  }
  html, body {
    margin: 0;
    width: 1200px;
    height: 1200px;
    overflow: hidden;
    background: var(--page-bg);
  }
  .tag {
    position: absolute;
    left: 50px;
    top: 275px;
    width: 1100px;
    height: 650px;
    border-radius: 6px;
    overflow: hidden;
    font-family: "PT Sans", sans-serif;
    box-shadow: 0 10px 30px rgba(0,0,0,0.18);
  }
  .tag__scene {
    position: absolute;
    inset: 0;
    background:
      linear-gradient(180deg, var(--sky-top) 0%, var(--sky-mid) 28%, var(--sky-glow) 44%, var(--ground) 52%, var(--ground-deep) 100%);
  }
  .tag__hole {
    position: absolute;
    right: -22px;
    top: 210px;
    width: 56px;
    height: 56px;
    border-radius: 50%;
    background: var(--page-bg);
  }
  .ghost-mark {
    position: absolute;
    left: 30px;
    top: 160px;
    width: 330px;
    height: 330px;
    box-sizing: border-box;
    border-radius: 50%;
    border: 4px solid var(--ghost);
    display: flex;
    align-items: center;
    justify-content: center;
    color: var(--ghost);
    font-size: 60px;
    font-weight: 700;
    letter-spacing: 2px;
  }
  .frame {
    position: absolute;
    left: 380px;
    top: 160px;
    width: 660px;
    height: 330px;
  }
  .cell {
    position: absolute;
    box-sizing: border-box;
    border: 6px solid var(--rule-white);
    color: var(--rule-white);
    display: flex;
    align-items: center;
    overflow: hidden;
  }
  .title {
    left: 0; top: 0; width: 660px; height: 150px;
    background: var(--band-orange);
    justify-content: center;
    font-size: 120px;
    font-weight: 700;
    letter-spacing: 3px;
    line-height: 1;
  }
  .web {
    left: 0; top: 144px; width: 486px; height: 86px;
    background: var(--band-orange);
    justify-content: center;
    font-size: 36px;
    font-weight: 700;
  }
  .year {
    left: 0; top: 224px; width: 150px; height: 96px;
    background: var(--band-dark);
    justify-content: center;
    font-size: 52px;
    font-weight: 700;
  }
  .strapline {
    left: 144px; top: 224px; width: 342px; height: 96px;
    background: var(--band-dark);
    padding: 0 14px 0 16px;
    font-family: "PT Sans Narrow", sans-serif;
    font-size: 24px;
    line-height: 1.2;
    text-transform: uppercase;
    letter-spacing: 0.5px;
  }
  .brand-box {
    left: 480px; top: 144px; width: 180px; height: 176px;
    background: var(--rule-white);
    justify-content: center;
    flex-direction: column;
    gap: 10px;
  }
  .brand-box__dot {
    width: 70px;
    height: 70px;
    border-radius: 50%;
    border: 3px solid var(--ink-dark);
  }
  .brand-box__name {
    color: var(--ink-dark);
    font-size: 28px;
    font-weight: 700;
  }
</style>
</head>
<body>
  <div class="tag">
    <div class="tag__scene" role="img" aria-label="Photograph of a runner leaping across a hilltop silhouetted against an orange sunset over water"></div>
    <div class="ghost-mark">RoamNest</div>
    <div class="frame">
      <div class="cell title">ROAMNEST</div>
      <div class="cell web">www.roamnest-example.uk</div>
      <div class="cell year">2018</div>
      <div class="cell strapline">Equipment and accessories<br>for backpackers</div>
      <div class="cell brand-box">
        <div class="brand-box__dot"></div>
        <div class="brand-box__name">RoamNest</div>
      </div>
    </div>
    <div class="tag__hole"></div>
  </div>
</body>
</html>
```